Card Design for my dog training business Rustpaw Obedience

Need a business card design for my dog training business with my new logo. Want the card to come off professional yet fun. Want it to be very eye catchy as well. I normally have these at vet clinics, pet stores, and groomers. so need it to look better than my competitors.
Target Market(s)
dog owners
Industry/Entity Type
Dog Training
Contact Information for Business Card
needs logo, my name and info
Font styles to use
Serif
Colors
0255a3
ffffff
ec1f27
000000
333333
fbfbfb
Requirements
Must have
- Rustpaw Obedience
- Hollis Brandt
- 415 903 2267
- info@rustpawobedience.example
- www.rustpawobedience.example

```html
<!DOCTYPE html>
<html lang="en">
<head>
<meta charset="utf-8">
<title>Rustpaw Obedience – Business Card</title>
<link rel="stylesheet" href="https://fonts.googleapis.com/css2?family=Tinos&family=Lato:wght@400&display=swap">
<style>
  :root {
    --backdrop: #ece8e2;
    --kraft-light: #d6b184;
    --kraft-mid: #c69c6c;
    --kraft-dark: #b98c5c;
    --ink: #1c1712;
    --card-shadow: rgba(40, 25, 10, 0.35);
  }
  * { margin: 0; padding: 0; box-sizing: border-box; }
  html, body {
    width: 1200px;
    height: 900px;
    overflow: hidden;
    background: var(--backdrop);
  }
  .canvas {
    position: relative;
    width: 1200px;
    height: 900px;
  }
  .card {
    position: absolute;
    left: 330px;
    width: 556px;
    height: 343px;
    background: radial-gradient(ellipse at 40% 15%, var(--kraft-light) 0%, var(--kraft-mid) 55%, var(--kraft-dark) 100%);
    box-shadow: 2px 3px 6px var(--card-shadow);
    color: var(--ink);
    text-align: center;
  }
  .card--front { top: 90px; }
  .card--back { top: 470px; }

  .holder-name {
    position: absolute;
    top: 84px;
    left: 0;
    right: 0;
    font-family: "Tinos", "Times New Roman", serif;
    font-size: 23px;
    letter-spacing: 0.5px;
  }
  .icon-row {
    position: absolute;
    top: 152px;
    left: 0;
    right: 0;
    display: flex;
    justify-content: center;
    align-items: center;
    gap: 6px;
  }
  .icon-row__rule {
    width: 58px;
    height: 2px;
    background: var(--ink);
    margin: 0 4px;
  }
  .icon-row svg { display: block; }
  .contact-list {
    position: absolute;
    top: 186px;
    left: 0;
    right: 0;
    list-style: none;
    font-family: "Lato", Arial, sans-serif;
    font-size: 18px;
    line-height: 24.5px;
  }

  .brand {
    position: absolute;
    top: 146px;
    left: 0;
    right: 0;
    display: flex;
    justify-content: center;
    align-items: center;
    gap: 12px;
  }
  .brand__mark {
    width: 16px;
    height: 16px;
    background: var(--ink);
  }
  .brand__name {
    font-family: "Tinos", "Times New Roman", serif;
    font-size: 34px;
    color: var(--ink);
    letter-spacing: 1px;
  }
</style>
</head>
<body>
<main class="canvas">
  <section class="card card--front">
    <h1 class="holder-name">HOLLIS BRANDT</h1>
    <div class="icon-row">
      <span class="icon-row__rule"></span>
      <svg class="icon icon--phone" width="24" height="24" viewBox="0 0 24 24" aria-label="Phone">
        <rect width="24" height="24" fill="var(--ink)"/>
        <path d="M6 9c0-2 2-3 6-3s6 1 6 3v1h-3V8.5h-6V10H6z" fill="var(--kraft-light)"/>
        <rect x="7" y="11" width="10" height="7" rx="1" fill="var(--kraft-light)"/>
        <circle cx="12" cy="14.5" r="1.8" fill="var(--ink)"/>
      </svg>
      <svg class="icon icon--mail" width="24" height="24" viewBox="0 0 24 24" aria-label="Email">
        <rect width="24" height="24" fill="var(--ink)"/>
        <rect x="5" y="7" width="14" height="10" fill="var(--kraft-light)"/>
        <path d="M5 7l7 6 7-6" fill="none" stroke="var(--ink)" stroke-width="1.3"/>
      </svg>
      <svg class="icon icon--web" width="24" height="24" viewBox="0 0 24 24" aria-label="Website">
        <rect width="24" height="24" fill="var(--ink)"/>
        <circle cx="12" cy="12" r="7" fill="var(--kraft-light)"/>
        <ellipse cx="12" cy="12" rx="3" ry="7" fill="none" stroke="var(--ink)" stroke-width="1"/>
        <line x1="5" y1="12" x2="19" y2="12" stroke="var(--ink)" stroke-width="1"/>
      </svg>
      <span class="icon-row__rule"></span>
    </div>
    <ul class="contact-list">
      <li class="contact-list__phone">415 903 2267</li>
      <li class="contact-list__email">info@rustpawobedience.example</li>
      <li class="contact-list__web">www.rustpawobedience.example</li>
    </ul>
  </section>

  <section class="card card--back">
    <div class="brand">
      <span class="brand__mark"></span>
      <span class="brand__name">Rustpaw Obedience</span>
    </div>
  </section>
</main>
</body>
</html>
```